Criação de Papelaria Profissional para Construção & Engenharia
" Fabricamos estruturas metálicas para Armazéns Graneleiros, Unidades de Beneficiamento de Sementes, Garagem para máquinas agrícolas, Classificação, etc "

```html
<!DOCTYPE html>
<html lang="pt-BR">
<head>
<meta charset="UTF-8">
<title>Ferravale – Papel Timbrado</title>
<link href="https://fonts.googleapis.com/css2?family=Roboto+Condensed:wght@400;700&display=swap" rel="stylesheet">
<style>
  :root {
    --backdrop: #e7e4df;
    --paper: #ffffff;
    --brand-red: #e0161b;
    --ink: #222222;
    --ink-soft: #555555;
  }
  * { box-sizing: border-box; margin: 0; padding: 0; }
  html, body {
    width: 1200px; height: 1200px; overflow: hidden;
    background: var(--backdrop);
    font-family: "Roboto Condensed", Arial, sans-serif;
  }
  .letterhead {
    position: absolute;
    left: 211px; top: 50px;
    width: 778px; height: 1100px;
    background: var(--paper);
    box-shadow: 0 6px 24px rgba(0,0,0,.18);
  }
  .letterhead__edge {
    position: absolute; left: 0; top: 0; bottom: 0;
    width: 12px; background: var(--brand-red);
  }
  .brand {
    position: absolute; left: 110px; top: 92px;
    display: flex; align-items: center; gap: 12px;
  }
  .brand__square {
    width: 22px; height: 22px; background: var(--brand-red); flex: none;
  }
  .brand__name {
    font-weight: 700; font-size: 40px; letter-spacing: 0.5px;
    color: var(--ink); line-height: 1;
  }
  .footer {
    position: absolute; left: 250px; right: 40px; bottom: 34px;
    display: flex; justify-content: space-between; align-items: flex-end;
    font-size: 13px; color: var(--ink-soft); line-height: 1.6;
  }
  .footer__item { display: flex; align-items: center; gap: 6px; }
  .footer__icon { width: 12px; height: 12px; flex: none; }
  .footer__address { text-align: right; font-style: normal; }
</style>
</head>
<body>
  <main class="letterhead">
    <div class="letterhead__edge"></div>

    <header class="brand">
      <span class="brand__square"></span>
      <span class="brand__name">Ferravale</span>
    </header>

    <footer class="footer">
      <div class="footer__phones">
        <div class="footer__item">(31) 90412-7765
          <svg class="footer__icon" viewBox="0 0 24 24"><path fill="#e0161b" d="M6.6 10.8a15 15 0 0 0 6.6 6.6l2.2-2.2c.3-.3.7-.4 1-.2 1.1.4 2.3.6 3.6.6.6 0 1 .4 1 1V20c0 .6-.4 1-1 1A17 17 0 0 1 3 4c0-.6.4-1 1-1h3.5c.6 0 1 .4 1 1 0 1.3.2 2.5.6 3.6.1.3 0 .7-.2 1z"/></svg>
        </div>
        <div class="footer__item">(31) 93308-2190
          <svg class="footer__icon" viewBox="0 0 24 24"><path fill="#e0161b" d="M6.6 10.8a15 15 0 0 0 6.6 6.6l2.2-2.2c.3-.3.7-.4 1-.2 1.1.4 2.3.6 3.6.6.6 0 1 .4 1 1V20c0 .6-.4 1-1 1A17 17 0 0 1 3 4c0-.6.4-1 1-1h3.5c.6 0 1 .4 1 1 0 1.3.2 2.5.6 3.6.1.3 0 .7-.2 1z"/></svg>
        </div>
      </div>
      <div class="footer__web">
        <div class="footer__item">contato@ferravale.com.br
          <svg class="footer__icon" viewBox="0 0 24 24"><rect x="2" y="5" width="20" height="14" rx="2" fill="#e0161b"/><path d="M3 7l9 6 9-6" fill="none" stroke="#fff" stroke-width="2"/></svg>
        </div>
        <div class="footer__item">www.ferravale.com.br
          <svg class="footer__icon" viewBox="0 0 24 24"><circle cx="12" cy="12" r="10" fill="#e0161b"/><path d="M2 12h20M12 2c3 3 3 17 0 20M12 2c-3 3-3 17 0 20" fill="none" stroke="#fff" stroke-width="1.5"/></svg>
        </div>
      </div>
      <address class="footer__address">
        <div class="footer__item">Av. das Acácias, N° 482 - Centro
          <svg class="footer__icon" viewBox="0 0 24 24"><path fill="#e0161b" d="M12 2a7 7 0 0 0-7 7c0 5 7 13 7 13s7-8 7-13a7 7 0 0 0-7-7zm0 9.5a2.5 2.5 0 1 1 0-5 2.5 2.5 0 0 1 0 5z"/></svg>
        </div>
        <div>Vale Alto/SP CEP 13540-210</div>
      </address>
    </footer>
  </main>
</body>
</html>
```